Podcast cover art (not a logo)

I’m launching an audio-only podcast for parents of neurodivergent children. The podcast is meant to feel like a calm, trusted professional voice — not a brand or a performance.

Style direction:
--Clean and minimal
--Calm and grounded
--Professional, not playful
--Nothing flashy, loud, or busy
--No cartoon imagery

Content on the cover:
--Podcast title: Under the Quiet Surface
--Subtitle or tagline: Supporting Neurodivergent Kids with Science, Not Shame (or Understanding Neurodivergent Kids)
--No episode numbers, no dates

Design preferences:
--Text-forward design
--Neutral or soft colors (muted blues, grays, off-whites)
--High contrast for readability at small sizes
--Simple, timeless font

What I do NOT want:
--A logo or branding system
--Illustrations of children or families
--Bright colors or playful graphics
--Trendy fonts or visual effects

Technical requirements:
--Square image
--3000 × 3000 pixels
--RGB color mode
--JPEG or PNG
--File size under 500 KB

Deliverables:
--Final cover art file
--Optional: one or two alternate background color versions

```html
<!DOCTYPE html>
<html lang="en">
<head>
<meta charset="utf-8">
<title>Under the Quiet Surface — Podcast Cover</title>
<link href="https://fonts.googleapis.com/css2?family=Anton&family=Oswald:wght@500&family=Roboto:wght@500&display=swap" rel="stylesheet">
<style>
  :root {
    --paper: #e6e7e9;
    --band: #67869a;
    --tag: #363638;
    --title: #ffffff;
    --ink: #38383b;
    --photo-light: #d3d4d7;
    --photo-mid: #b9bbbf;
  }
  html, body {
    margin: 0;
    padding: 0;
    width: 1200px;
    height: 1200px;
    overflow: hidden;
    background: var(--paper);
  }
  .cover {
    position: relative;
    width: 1200px;
    height: 1200px;
    background: var(--paper);
  }
  .cover-art {
    position: absolute;
    inset: 0;
    width: 1200px;
    height: 1200px;
  }
  .band { fill: var(--band); }
  .tag { fill: var(--tag); }
  .title-word {
    font-family: "Anton", "Oswald", sans-serif;
    fill: var(--title);
  }
  .title-joiner {
    font-family: "Oswald", "Roboto Condensed", sans-serif;
    font-weight: 500;
    fill: var(--title);
  }
  .tagline {
    position: absolute;
    left: 0;
    right: 0;
    top: 1066px;
    margin: 0;
    text-align: center;
    font-family: "Roboto", Arial, sans-serif;
    font-weight: 500;
    font-size: 34px;
    line-height: 42px;
    letter-spacing: 0.2px;
    color: var(--ink);
  }
</style>
</head>
<body>
<main class="cover">
  <svg class="cover-art" viewBox="0 0 1200 1200" xmlns="http://www.w3.org/2000/svg">
    <defs>
      <linearGradient id="photoTone" x1="0" y1="0" x2="1" y2="0">
        <stop offset="0" stop-color="var(--photo-mid)"/>
        <stop offset="0.5" stop-color="var(--photo-light)"/>
        <stop offset="1" stop-color="var(--photo-mid)"/>
      </linearGradient>
    </defs>

    <rect class="photo-area" x="460" y="24" width="280" height="498" fill="url(#photoTone)" role="img" aria-label="Photograph of a silver vintage studio microphone on a stand"/>

    <polygon class="band" points="130,522 934,522 865,768 61,768"/>
    <text class="title-word" x="502" y="723" font-size="210" text-anchor="middle" textLength="600" lengthAdjust="spacingAndGlyphs">UNDER</text>

    <polygon class="band" points="301,778 1138,778 1069,1023 231,1023"/>
    <text class="title-word" x="677" y="984" font-size="210" text-anchor="middle" textLength="745" lengthAdjust="spacingAndGlyphs">SURFACE</text>

    <polygon class="tag" points="430,720 800,720 768,829 398,829"/>
    <text class="title-joiner" x="599" y="808" font-size="86" text-anchor="middle" textLength="290" lengthAdjust="spacingAndGlyphs">THE QUIET</text>
  </svg>

  <p class="tagline">Supporting Neurodivergent Kids with Science, Not Shame<br>(or Understanding Neurodivergent Kids)</p>
</main>
</body>
</html>
```